we need a design for Water Bottle Lable Wrap
The product is called Corvane Water is a restructured water. its a very healthy and rejuvenating water
we were looking at using as a tag ling Restore, Recover, Rejuvenate.

```html
<!DOCTYPE html>
<html lang="en">
<head>
<meta charset="utf-8">
<title>Corvane Water – Bottle Label</title>
<link href="https://fonts.googleapis.com/css2?family=Montserrat:wght@400;500&display=swap" rel="stylesheet">
<style>
  :root {
    --backdrop: #1f5f9a;
    --backdrop-light: #2a73b3;
    --navy: #1b3f7a;
    --sky-pale: #e9f3fc;
    --sky-mid: #9cc7ee;
    --water-bright: #3d8fe0;
    --water-deep: #1357c4;
    --water-dark: #0d44a8;
    --white: #ffffff;
  }
  * { margin: 0; padding: 0; box-sizing: border-box; }
  html, body {
    width: 778px;
    height: 1200px;
    overflow: hidden;
  }
  body {
    background: radial-gradient(ellipse at 50% 35%, var(--backdrop-light) 0%, var(--backdrop) 70%);
    position: relative;
  }
  .label {
    position: absolute;
    left: 109px;
    top: 315px;
    width: 560px;
    height: 570px;
    overflow: hidden;
    background: radial-gradient(ellipse at 50% 20%, var(--white) 0%, var(--sky-pale) 35%, var(--sky-mid) 100%);
    box-shadow: 0 10px 30px rgba(0, 0, 0, 0.25);
  }
  .label__brand {
    position: absolute;
    left: 0;
    top: 70px;
    width: 100%;
    padding: 0 58px;
    font-family: "Montserrat", sans-serif;
    font-weight: 400;
    color: var(--navy);
  }
  .label__name {
    display: block;
    font-size: 104px;
    line-height: 1.1;
    font-weight: 400;
  }
  .label__water {
    display: block;
    text-align: right;
    font-size: 68px;
    line-height: 1.1;
    font-weight: 400;
  }
  .label__splash {
    position: absolute;
    left: 0;
    top: 300px;
    width: 100%;
    height: 270px;
    background: linear-gradient(180deg, var(--sky-mid) 0%, var(--water-bright) 25%, var(--water-deep) 60%, var(--water-dark) 100%);
  }
  .label__tagline {
    position: absolute;
    left: 0;
    right: 0;
    bottom: 34px;
    text-align: center;
    font-family: "Montserrat", sans-serif;
    font-weight: 500;
    font-size: 28px;
    color: var(--white);
    letter-spacing: 0.5px;
  }
</style>
</head>
<body>
  <section class="label">
    <div class="label__splash" role="img" aria-label="Photo of a sunlit water surface with splashing droplets"></div>
    <h1 class="label__brand">
      <span class="label__name">Corvane</span>
      <span class="label__water">Water</span>
    </h1>
    <p class="label__tagline">Restore | Recover | Rejuvenate</p>
  </section>
</body>
</html>
```